依頼詳細
完成見学会にて使用する【のぼり旗】のデザインを募集いたします。
600x1800のサイズで【月々5万円台から(~でも可)】【ZEH】【注文住宅専門店】の3つを分かりやすく目に入りやすいデザインで作成をお願いします。
それぞれのキーワードの前後に言葉を付け加えても、無くても結構です。
(例)月々5万円台からの注文住宅!、月々5万円台からのマイホーム!
高性能 ZEH!、省エネ×創エネ ZEH!
手が届く注文住宅!など

色合いとフォントは弊社のロゴマークに合うようにお願いします。
文字の配置や大きさ等は、添付データに沿ったデザインではなくて結構です。
記載項目
キャッチフレーズ、注文住宅専門店、ロゴマーク、そよみねホーム記載の検索窓イメージ

サイズ→600x1800
希望イメージ
シンプル 複雑
単色 カラフル
暗い 明るい
日常 高級
遊び心 厳粛
未来的 伝統的
女性的 男性的
希望する色
黄・オレンジ系、緑系、茶系、添付ロゴに沿った色合い
納品ファイル
• 高解像度JPG (.jpg)
• イラストレーター形式 (.ai)
• フォトショップ形式 (.psd)
• PNG形式 (.png)
補足説明
のぼり旗で使用するロゴデータを追記しました。
よろしくお願いします。
■ 選んだ理由

掲載して欲しいキーワードが分かりやすかったため選びました。
配色も社内で評判が良く、文字も見やすかったです。

■ 提案者全員のお礼・コメント

沢山のステキなご提案をありがとうございました。
また機会がありましたら宜しくお願いいたします。

```html
<!DOCTYPE html>
<html lang="ja">
<head>
<meta charset="UTF-8">
<title>ZEH 注文住宅 のぼり旗 | そよみねホーム</title>
<link rel="stylesheet" href="https://fonts.googleapis.com/css2?family=M+PLUS+Rounded+1c:wght@500;800;900&family=Quicksand:wght@500&display=swap">
<style>
  :root {
    --green: #8cc63f;
    --yellow: #fff100;
    --brown: #8b6e4e;
    --orange: #f39800;
    --zeh: #6e6057;
    --white: #ffffff;
    --ink: #111111;
    --rule: #8a7f78;
    --mascot: #c9a06a;
  }
  * { margin: 0; padding: 0; box-sizing: border-box; }
  html, body { width: 1200px; height: 3580px; overflow: hidden; background: var(--white); }
  .banner {
    position: relative; width: 1200px; height: 3580px; overflow: hidden;
    background: var(--white);
    font-family: "M PLUS Rounded 1c", sans-serif;
  }
  .house-shape { position: absolute; left: 0; top: 0; }

  .tag {
    position: absolute; top: 72px; height: 136px; width: 290px;
    color: var(--white); font-weight: 800; font-size: 88px;
    display: flex; align-items: center; justify-content: center;
    letter-spacing: 2px;
  }
  .tag--insulation { left: 75px; width: 265px; background: var(--brown); }
  .tag--saving { left: 400px; background: var(--green); }
  .tag--creation { left: 755px; background: var(--orange); }

  .zeh-title {
    position: absolute; top: 225px; left: 0; width: 1200px; text-align: center;
    font-family: "Quicksand", sans-serif; font-weight: 500;
    font-size: 440px; line-height: 1; letter-spacing: 40px; padding-left: 40px;
    color: var(--zeh);
  }
  .zeh-reading {
    position: absolute; top: 660px; left: 120px; width: 960px;
    display: flex; align-items: center; gap: 40px;
    color: var(--zeh); font-size: 72px; font-weight: 500;
  }
  .zeh-reading::before, .zeh-reading::after {
    content: ""; flex: 1; height: 5px; background: var(--rule);
  }

  .price-five {
    position: absolute; left: 120px; top: 1060px;
    font-size: 960px; font-weight: 900; line-height: 1; color: var(--yellow);
  }
  .price-monthly {
    position: absolute; left: 735px; top: 1165px; width: 305px; height: 220px;
    background: var(--white); color: var(--green);
    font-size: 150px; font-weight: 900; line-height: 220px; text-align: center;
  }
  .price-amount {
    position: absolute; left: 715px; top: 1430px;
    color: var(--white); font-weight: 900; font-size: 168px; line-height: 1.05;
  }
  .price-from {
    position: absolute; left: 718px; top: 1625px;
    color: var(--white); font-weight: 900; font-size: 130px; line-height: 1;
  }

  .custom-home {
    position: absolute; left: 100px; top: 1850px; width: 1000px;
    display: grid; grid-template-columns: 500px 500px; row-gap: 20px;
    color: var(--white); font-weight: 900; font-size: 470px; line-height: 1;
    text-align: center;
  }

  .click-cue {
    position: absolute; left: 690px; top: 2920px;
    font-family: "Quicksand", sans-serif; font-size: 68px; color: var(--ink);
    transform: rotate(-12deg);
  }
  .search-box {
    position: absolute; left: 40px; top: 3065px; width: 820px; height: 100px;
    display: flex; border: 5px solid var(--ink); background: var(--white);
  }
  .search-box__field {
    flex: 1; display: flex; align-items: center; padding-left: 40px;
    font-size: 66px; font-weight: 800; color: var(--ink);
  }
  .search-box__button {
    width: 200px; background: var(--ink); color: var(--white);
    font-size: 62px; font-weight: 800; display: flex; align-items: center; padding-left: 28px;
  }
  .mascot {
    position: absolute; left: 860px; top: 2820px; width: 310px; height: 390px;
    border-radius: 120px 120px 60px 60px;
    background: linear-gradient(180deg, #c8623c 0%, #e9a56a 40%, var(--mascot) 100%);
  }

  .brand {
    position: absolute; left: 0; top: 3290px; width: 1200px; height: 220px;
    display: flex; align-items: center; justify-content: center; gap: 40px;
  }
  .brand__mark { width: 150px; height: 150px; background: var(--brown); }
  .brand__name { font-size: 130px; font-weight: 800; color: var(--brown); letter-spacing: 4px; }
</style>
</head>
<body>
<main class="banner">
  <svg class="house-shape" width="1200" height="3210" viewBox="0 0 1200 3210" aria-hidden="true">
    <polygon fill="var(--green)" points="0,1100 190,1049 190,850 300,850 300,1020 1200,780 1200,3210 0,3210"/>
  </svg>

  <div class="tag tag--insulation">断熱</div>
  <div class="tag tag--saving">省エネ</div>
  <div class="tag tag--creation">創エネ</div>

  <h1 class="zeh-title">ZEH</h1>
  <p class="zeh-reading">ゼッチ</p>

  <div class="price-five">5</div>
  <div class="price-monthly">月々</div>
  <div class="price-amount">万円</div>
  <div class="price-from">からの</div>

  <h2 class="custom-home"><span>注</span><span>文</span><span>住</span><span>宅</span></h2>

  <div class="click-cue">\click/</div>
  <div class="search-box">
    <div class="search-box__field">そよみねホーム</div>
    <div class="search-box__button">検索</div>
  </div>
  <div class="mascot" role="img" aria-label="木の家をかぶったマスコットキャラクターのイラスト"></div>

  <div class="brand">
    <span class="brand__mark" aria-hidden="true"></span>
    <span class="brand__name">そよみねホーム</span>
  </div>
</main>
</body>
</html>
```